3 x Professional Herbal Supplement Label Design Ready to Print in UK Standard + Example inc

Hi,
Thank you for taking the time to read. I'm looking for an excellent graphic designer experienced in creating supplement labels for our 3 new products. The labels should be sized and have the resolution ready for the printers.
Here is the work:
I'm looking for a new supplement label design that I can use for 3 new products called:
1 - Raspberry Ketone
2 - Garcinia Cambogia
3 - Green Coffee
You will only need to create a single label to enter the competition, as the label created will be the template for all 3 products listed above. You can choose whether you go for product 1, 2,or 3 to enter the design competition, but all 3 will be required on completion should you be selected.
Simply, the label template would be adjusted for the other products, what would be different is the product specifics like, name, background graphic of the ingredient and ingredients listed, directions of use, barcode etc.
The design I like, which I'd like you to copy and then artistically make different is attached and titled "BrightMeadow_Garcinia_Cambogia_LABEL.jpg"
My company logo is attached called "vorix final logo.ai" & "vorix-invis.png" - Please let me know if this resolution is not suitable.
The guidance information in designing a UK label from the supplement manufacturer is attached, as follows:
The supplement manufacturer has also provided a very basic example of a product they produced for another company (Not very good I know, but at least shows what goes where). Please do not use this as an example of a good design!
*** I will provide more specific product detail (ingredients, bar-code, dosage) if your initial design is liked and selected for adjustment, as we will require that all 3 label designs are completed.
*** The delivered image files will need to be in Photoshop format.

```html
<!DOCTYPE html>
<html lang="en">
<head>
<meta charset="utf-8">
<title>vorix Supplement Labels</title>
<link href="https://fonts.googleapis.com/css2?family=Roboto:wght@400;500;700;900&display=swap" rel="stylesheet">
<style>
  :root {
    --bg: #eeeeef;
    --label-white: #ffffff;
    --tab-orange: #f5a623;
    --logo-blue: #2a9fd8;
    --ink-white: #ffffff;
    --badge-black: #1c1c1c;
    --band-green: #7cb342;
    --band-grey: #d9d9d9;

    --garcinia-red: #e3303f;
    --cambogia-green: #8cc63f;
    --garcinia-accent: #2b9ad9;
    --garcinia-photo-a: #c9dc7a;
    --garcinia-photo-b: #6a9a35;

    --raspberry-red: #e23058;
    --ketone-green: #7cc242;
    --raspberry-accent: #9b3a8c;
    --raspberry-photo-a: #f1738f;
    --raspberry-photo-b: #b8203f;

    --coffee-green: #7cb342;
    --coffee-brown: #8b5a2b;
    --coffee-accent: #5aa832;
    --coffee-photo-a: #9cc16a;
    --coffee-photo-b: #4e7a2c;
  }
  * { box-sizing: border-box; margin: 0; padding: 0; }
  html, body {
    width: 1200px; height: 741px; overflow: hidden;
    background: var(--bg);
    font-family: "Roboto", Arial, sans-serif;
  }
  .label-set {
    position: relative; width: 1200px; height: 741px;
  }
  .label {
    position: absolute; top: 150px;
    width: 340px; height: 440px;
    background: var(--label-white);
    overflow: hidden;
    border-radius: 4px;
    box-shadow: 0 2px 10px rgba(0,0,0,0.08);
  }
  .label--garcinia { left: 60px; --accent: var(--garcinia-accent); --photo-a: var(--garcinia-photo-a); --photo-b: var(--garcinia-photo-b); }
  .label--raspberry { left: 430px; --accent: var(--raspberry-accent); --photo-a: var(--raspberry-photo-a); --photo-b: var(--raspberry-photo-b); }
  .label--coffee { left: 800px; --accent: var(--coffee-accent); --photo-a: var(--coffee-photo-a); --photo-b: var(--coffee-photo-b); }

  .label__tab {
    position: absolute; top: 22px; left: 0;
    width: 44px; height: 12px; background: var(--tab-orange);
  }
  .brand {
    position: absolute; top: 34px; left: 0; right: 0;
    display: flex; justify-content: center; align-items: center; gap: 6px;
  }
  .brand__dot {
    width: 14px; height: 14px; border-radius: 50%; background: var(--logo-blue);
  }
  .brand__name {
    font-size: 26px; font-weight: 400; color: var(--logo-blue); letter-spacing: 0.5px;
  }
  .product-name {
    position: absolute; top: 76px; left: 0; right: 0;
    text-align: center; font-weight: 700; font-size: 38px; line-height: 40px;
    letter-spacing: 1px; text-transform: uppercase;
  }
  .product-name__line { display: block; }
  .label--garcinia .product-name__first { color: var(--garcinia-red); }
  .label--garcinia .product-name__second { color: var(--cambogia-green); }
  .label--raspberry .product-name__first { color: var(--raspberry-red); }
  .label--raspberry .product-name__second { color: var(--ketone-green); }
  .label--coffee .product-name__first { color: var(--coffee-green); }
  .label--coffee .product-name__second { color: var(--coffee-brown); }

  .product-tag {
    position: absolute; top: 166px; left: 50%; transform: translateX(-50%);
    background: var(--accent); color: var(--ink-white);
    font-size: 14px; padding: 4px 14px; border-radius: 12px; white-space: nowrap;
  }
  .ingredient-photo {
    position: absolute; top: 200px; left: 0; right: 0; height: 200px;
    background: radial-gradient(ellipse at 60% 45%, var(--photo-a), var(--photo-b) 80%, transparent 100%);
    opacity: 0.9;
  }
  .claim-swoosh {
    position: absolute; left: 0; bottom: 22px; width: 190px; height: 170px;
  }
  .claims {
    position: absolute; left: 14px; bottom: 50px;
    color: var(--ink-white); font-size: 15px; line-height: 17px;
  }
  .claims__item { display: block; }
  .claims__item--indent { padding-left: 34px; margin-top: 10px; }
  .count-badge {
    position: absolute; right: 40px; top: 272px;
    width: 52px; height: 60px; background: var(--badge-black);
    border-radius: 6px; color: var(--ink-white); text-align: center;
    padding-top: 6px;
  }
  .count-badge__number { display: block; font-size: 18px; font-weight: 700; line-height: 20px; }
  .count-badge__unit { display: block; font-size: 8px; line-height: 10px; margin-top: 2px; }
  .base-band {
    position: absolute; left: 0; right: 0; bottom: 0; height: 22px;
    background: linear-gradient(to bottom, var(--band-green) 0 60%, var(--band-grey) 60% 100%);
  }
</style>
</head>
<body>
<main class="label-set">

  <section class="label label--garcinia">
    <div class="label__tab"></div>
    <div class="brand"><span class="brand__dot"></span><span class="brand__name">vorix</span></div>
    <h1 class="product-name">
      <span class="product-name__line product-name__first">Garcinia</span>
      <span class="product-name__line product-name__second">Cambogia</span>
    </h1>
    <div class="product-tag">Whole Fruit Extract</div>
    <div class="ingredient-photo" role="img" aria-label="Photo of whole and halved garcinia cambogia fruits with leaves"></div>
    <svg class="claim-swoosh" viewBox="0 0 190 170" aria-hidden="true">
      <path d="M0 20 C70 0 140 20 190 70 L190 170 L0 170 Z" fill="var(--accent)"/>
    </svg>
    <p class="claims"><span class="claims__item">Advanced<br>Formula</span><span class="claims__item claims__item--indent">Maximum<br>Strength</span></p>
    <div class="count-badge"><span class="count-badge__number">120</span><span class="count-badge__unit">Vegetarian<br>Capsules</span></div>
    <div class="base-band"></div>
  </section>

  <section class="label label--raspberry">
    <div class="label__tab"></div>
    <div class="brand"><span class="brand__dot"></span><span class="brand__name">vorix</span></div>
    <h1 class="product-name">
      <span class="product-name__line product-name__first">Raspberry</span>
      <span class="product-name__line product-name__second">Ketone</span>
    </h1>
    <div class="product-tag">Natural Raspberry Ketones</div>
    <div class="ingredient-photo" role="img" aria-label="Photo of ripe raspberries with green leaves"></div>
    <svg class="claim-swoosh" viewBox="0 0 190 170" aria-hidden="true">
      <path d="M0 20 C70 0 140 20 190 70 L190 170 L0 170 Z" fill="var(--accent)"/>
    </svg>
    <p class="claims"><span class="claims__item">Advanced<br>Formula</span><span class="claims__item claims__item--indent">Maximum<br>Strength</span></p>
    <div class="count-badge"><span class="count-badge__number">120</span><span class="count-badge__unit">Vegetarian<br>Capsules</span></div>
    <div class="base-band"></div>
  </section>

  <section class="label label--coffee">
    <div class="label__tab"></div>
    <div class="brand"><span class="brand__dot"></span><span class="brand__name">vorix</span></div>
    <h1 class="product-name">
      <span class="product-name__line product-name__first">Green</span>
      <span class="product-name__line product-name__second">Coffee</span>
    </h1>
    <div class="product-tag">50% CHLOROGENIC ACID</div>
    <div class="ingredient-photo" role="img" aria-label="Photo of a pile of green coffee beans"></div>
    <svg class="claim-swoosh" viewBox="0 0 190 170" aria-hidden="true">
      <path d="M0 20 C70 0 140 20 190 70 L190 170 L0 170 Z" fill="var(--accent)"/>
    </svg>
    <p class="claims"><span class="claims__item">Advanced<br>Formula</span><span class="claims__item claims__item--indent">Maximum<br>Strength</span></p>
    <div class="count-badge"><span class="count-badge__number">120</span><span class="count-badge__unit">Vegetarian<br>Capsules</span></div>
    <div class="base-band"></div>
  </section>

</main>
</body>
</html>
```